Recruitment of Brindle Staffing for the UK market

I want a website for the UK market to attract businesses and companies to come to us for Philipine labour. We want an information site that gives all information on what we do and how we can recruit Philippine labour.
This is a recruitment site for companies to contact us with their requirements for skilled workers coming from the Philipines over to the UK to work.

Target Market(s)

Uk Companies and businesses who want Philipine skilled workers

Industry/Entity Type

REcruitment

Coding

Coded - Design and coding required

Number of Pages Required

5+ page

Font styles to use
Sans Serif

Colors
0054AA
0677BA
7BADD7
CADEEF
E8F1F8
0094D4
00A9DD
6FCCEA
C7EBF8
E9F6FB
EE7325
F08F49
F5BC92
FAE3D3
FDF4ED
EB3D1F
EC4F4E
F09395
F8D3D4
FCEDEE

Requirements
Must have
• Look professional and corperate with drop down menus for Home ,about, services,articles. training , contact us
Nice to have
• Look at Tovel recruitment- https://tovelrecruitment.example.co.uk/. This is my current site - https://www.brindlestaffing.example.com/
Should not have
• Cartoons or silly pictures , needs to be corperate looking

```html
<!DOCTYPE html>
<html lang="en">
<head>
<meta charset="utf-8">
<title>Brindle Staffing – Skilled Philippine Workers for UK Companies</title>
<link rel="stylesheet" href="https://fonts.googleapis.com/css2?family=Barlow:wght@400;500;600;700&display=swap">
<style>
:root{
  --blue:#0054AA;
  --blue-mid:#0677BA;
  --blue-pale:#E8F1F8;
  --teal:#26BED1;
  --orange:#EE7325;
  --orange-light:#F08F49;
  --orange-pale:#FAE3D3;
  --red:#EB3D1F;
  --red-soft:#F09395;
  --red-pale:#F8D3D4;
  --ink:#111418;
  --muted:#6b6f76;
  --line:#d9dce1;
  --white:#ffffff;
}
*{box-sizing:border-box;margin:0;padding:0}
html,body{width:1200px;height:3706px;overflow:hidden}
body{position:relative;background:var(--white);font-family:'Barlow',Arial,sans-serif;color:var(--ink)}
.abs{position:absolute}
.btn{position:absolute;display:flex;align-items:center;justify-content:center;border-radius:4px;font-weight:500;font-size:14px}
.btn-blue{background:var(--blue);color:var(--white)}
.btn-outline{border:1.5px solid var(--ink);color:var(--ink);background:var(--white)}

/* header & hero */
.hero{left:0;top:0;width:1200px;height:639px;background:linear-gradient(90deg,#eef3f8 0%,#e7eef6 40%,#c9d3de 100%)}
.hero-photo{left:560px;top:0;width:640px;height:639px;background:radial-gradient(ellipse at 55% 45%,#d7b7a0 0%,#9a8a84 35%,#5d6f86 65%,#c4ccd6 100%);opacity:.85}
.hero-fade{left:420px;top:0;width:300px;height:639px;background:linear-gradient(90deg,#eaf0f6,rgba(234,240,246,0))}
.logo{left:127px;top:48px;display:flex;align-items:center;gap:8px;font-weight:700;font-size:20px;color:var(--red)}
.logo-mark{width:20px;height:20px;background:var(--red);border-radius:50%}
.nav{left:501px;top:44px;display:flex;gap:26px;font-size:13px;font-weight:500}
.hero h1{left:122px;top:205px;font-size:46px;line-height:51px;font-weight:600;letter-spacing:-.3px}
.hero h1 em{font-style:normal;color:var(--red)}
.search{left:127px;top:450px;width:506px;height:65px;background:var(--white);border-radius:4px;box-shadow:0 6px 18px rgba(0,0,0,.08)}
.search-field{position:absolute;top:24px;font-size:12.5px;font-weight:500;display:flex;align-items:center;gap:8px}

/* featured jobs */
.section-title{font-size:32px;font-weight:600;letter-spacing:-.2px}
.job{width:306px;height:251px;background:var(--white);box-shadow:0 2px 14px rgba(0,0,0,.08);border-radius:3px}
.job-icon{position:absolute;left:12px;top:12px;width:42px;height:42px;border-radius:4px;box-shadow:0 1px 6px rgba(0,0,0,.1);display:flex;align-items:center;justify-content:center}
.job-icon span{width:18px;height:18px;border-radius:50%;background:var(--red)}
.job-company{position:absolute;left:70px;top:18px;font-size:18px;font-weight:600}
.job-country{position:absolute;left:70px;top:42px;font-size:17px;color:var(--muted)}
.job-title{position:absolute;left:14px;top:82px;font-size:16px;font-weight:500}
.job-type{position:absolute;left:14px;top:104px;font-size:12px;color:var(--muted)}
.job-desc{position:absolute;left:14px;top:124px;width:282px;font-size:11.5px;line-height:18px;color:var(--muted)}
.job-pay{position:absolute;left:14px;top:208px;font-size:16px;font-weight:500;color:var(--red)}
.job .btn{left:196px;top:207px;width:92px;height:33px;font-size:13px;border-radius:5px}

/* how it works */
.step{left:121px;display:flex;align-items:center;gap:14px}
.step-num{width:32px;height:32px;border-radius:50%;display:flex;align-items:center;justify-content:center;font-size:15px;font-weight:600;background:var(--red-soft);color:var(--red)}
.step-num.active{background:var(--red);color:var(--white)}
.step-title{font-size:16px;font-weight:500}
.step.active .step-title{color:var(--red)}
.step-sub{font-size:9px;color:#444}
.step-line{left:137px;width:1px;height:22px;background:var(--red-soft)}
.contact{left:633px;top:1321px;width:443px;height:386px;background:var(--teal)}
.contact-card{left:666px;top:1347px;width:377px;height:334px;background:var(--white)}
.contact-card h3{position:absolute;left:36px;top:16px;font-size:22px;font-weight:600}
.field{position:absolute;left:36px;width:292px;height:35px;border:1.2px solid #222;border-radius:4px;font-size:12px;padding:10px 8px}
.contact-card .btn{left:36px;top:286px;width:110px;height:35px;font-size:12px}

/* business */
.photo{border-radius:2px}
.badge{left:436px;top:1793px;width:161px;height:79px;background:var(--red);color:var(--white);padding:10px 20px}
.badge b{display:block;font-size:27px;font-weight:500;line-height:30px}
.badge span{font-size:15px}
.body-copy{font-size:13.5px;line-height:19.2px;color:#333}
.recruit{left:121px;top:2157px;font-size:31px;line-height:39px;font-weight:600;letter-spacing:-.2px}
.recruit em{font-style:normal;color:var(--red)}

/* talent */
.talent{top:2566px;width:235px;height:341px;background:var(--white);box-shadow:0 2px 14px rgba(0,0,0,.08)}
.talent-photo{position:absolute;left:12px;top:13px;width:211px;height:250px}
.rating{position:absolute;right:20px;top:21px;background:var(--white);border-radius:8px;font-size:9px;font-weight:600;padding:1px 5px}
.rating i{font-style:normal;color:#f5b50a}
.talent-role{position:absolute;left:18px;top:276px;font-size:11px;color:var(--muted)}
.talent-name{position:absolute;left:18px;top:291px;font-size:17px;font-weight:600}
.talent-age{position:absolute;left:18px;top:312px;font-size:12px;color:var(--muted)}
.dot{top:2940px;width:9px;height:9px;border-radius:50%;background:#777}
.dot.on{background:#111}

/* footer */
.footer{left:0;top:3396px;width:1200px;height:268px;background:linear-gradient(180deg,var(--orange-light),var(--orange))}
.footer h4{position:absolute;top:74px;font-size:17px;font-weight:500;color:var(--ink)}
.footer ul{position:absolute;list-style:none;font-size:11.5px;line-height:18px;color:#1d1d1d}
.newsletter{left:121px;top:109px;width:406px;height:46px;background:#fdf4ed;border:1px solid var(--white);border-radius:3px}
.contact-row{position:absolute;left:590px;display:flex;gap:10px;font-size:11.5px;line-height:16px;color:#1d1d1d}
.bottom-bar{left:0;top:3664px;width:1200px;height:42px;background:var(--red);color:var(--white);font-size:11px}
.social{top:11px;width:21px;height:21px;border-radius:50%;background:var(--white)}
</style>
</head>
<body>

<!-- header & hero -->
<section class="abs hero">
  <div class="abs hero-photo" role="img" aria-label="Smiling young man in glasses and a checked shirt talking on a phone"></div>
  <div class="abs hero-fade"></div>
  <div class="abs logo"><span class="logo-mark"></span>Brindle Staffing</div>
  <nav class="abs nav"><span>Home</span><span>Post Job</span><span>Find a Job</span></nav>
  <div class="btn btn-outline" style="left:814px;top:32px;width:108px;height:37px;border-radius:4px">Login</div>
  <div class="btn btn-blue" style="left:932px;top:32px;width:158px;height:40px">Create an Account</div>
  <h1 class="abs">Recruiting and placing<br>skilled <em>Philippine workers</em><br>into UK companies</h1>
  <div class="abs search">
    <div class="search-field" style="left:20px">
      <svg width="16" height="16" viewBox="0 0 16 16"><circle cx="6.5" cy="6.5" r="5" fill="none" stroke="#111" stroke-width="1.5"/><path d="M10.5 10.5L15 15" stroke="#111" stroke-width="1.5"/></svg>
      Job Title or Company
    </div>
    <div class="abs" style="left:183px;top:18px;width:1px;height:28px;background:var(--line)"></div>
    <div class="search-field" style="left:200px">
      <svg width="12" height="16" viewBox="0 0 12 16"><path d="M6 1a5 5 0 0 0-5 5c0 4 5 9 5 9s5-5 5-9a5 5 0 0 0-5-5z" fill="none" stroke="#111" stroke-width="1.3"/><circle cx="6" cy="6" r="1.8" fill="none" stroke="#111" stroke-width="1.2"/></svg>
      Select Country
      <svg width="10" height="6" viewBox="0 0 10 6" style="margin-left:28px"><path d="M1 1l4 4 4-4" fill="none" stroke="#111" stroke-width="1.3"/></svg>
    </div>
    <div class="btn btn-blue" style="left:394px;top:12px;width:105px;height:46px;font-size:13px">Search</div>
  </div>
</section>

<!-- featured jobs -->
<h2 class="abs section-title" style="left:121px;top:674px">Featured Job</h2>
<div class="btn btn-blue" style="left:963px;top:672px;width:113px;height:45px;font-size:13px;font-weight:600">Find More Jobs</div>

<article class="abs job" style="left:122px;top:745px">
  <div class="job-icon"><span></span></div><div class="job-company">Northvale Corp</div><div class="job-country">U.K</div>
  <div class="job-title">Data Analyst</div><div class="job-type">Full-time</div>
  <p class="job-desc">Lorem ipsum dolor sit amet, consectetur adipis-cing elit, sed do eiusmod tempor incididunt ut labore et dolore magna aliqua. Quis ipsum sus-pendisse ultrices gravida. Risus commodo viverra</p>
  <div class="job-pay">$200/Month</div><div class="btn btn-outline">Apply Now</div>
</article>
<article class="abs job" style="left:449px;top:745px">
  <div class="job-icon"><span></span></div><div class="job-company">Larkfield Foods</div><div class="job-country">U.K</div>
  <div class="job-title">Civil Engineer</div><div class="job-type">Full-time</div>
  <p class="job-desc">Lorem ipsum dolor sit amet, consectetur adipis-cing elit, sed do eiusmod tempor incididunt ut labore et dolore magna aliqua. Quis ipsum sus-pendisse ultrices gravida. Risus commodo viverra</p>
  <div class="job-pay">$400/Month</div><div class="btn btn-outline">Apply Now</div>
</article>
<article class="abs job" style="left:774px;top:745px">
  <div class="job-icon"><span></span></div><div class="job-company">Meadow Hospital</div><div class="job-country">U.K</div>
  <div class="job-title">Criminologist</div><div class="job-type">Full-time</div>
  <p class="job-desc">Lorem ipsum dolor sit amet, consectetur adipis-cing elit, sed do eiusmod tempor incididunt ut labore et dolore magna aliqua. Quis ipsum sus-pendisse ultrices gravida. Risus commodo viverra</p>
  <div class="job-pay">$200/Month</div><div class="btn btn-outline">Apply Now</div>
</article>
<article class="abs job" style="left:122px;top:1016px">
  <div class="job-icon"><span></span></div><div class="job-company">Northvale Corp</div><div class="job-country">U.K</div>
  <div class="job-title">Anthropologist</div><div class="job-type">Full-time</div>
  <p class="job-desc">Lorem ipsum dolor sit amet, consectetur adipis-cing elit, sed do eiusmod tempor incididunt ut labore et dolore magna aliqua. Quis ipsum sus-pendisse ultrices gravida. Risus commodo viverra</p>
  <div class="job-pay">$200/Month</div><div class="btn btn-outline">Apply Now</div>
</article>
<article class="abs job" style="left:449px;top:1016px">
  <div class="job-icon"><span></span></div><div class="job-company">Halden Works</div><div class="job-country">U.K</div>
  <div class="job-title">Highway Engineer</div><div class="job-type">Full-time</div>
  <p class="job-desc">Lorem ipsum dolor sit amet, consectetur adipis-cing elit, sed do eiusmod tempor incididunt ut labore et dolore magna aliqua. Quis ipsum sus-pendisse ultrices gravida. Risus commodo viverra</p>
  <div class="job-pay">$200/Month</div><div class="btn btn-outline">Apply Now</div>
</article>
<article class="abs job" style="left:774px;top:1016px">
  <div class="job-icon"><span></span></div><div class="job-company">Northvale Corp</div><div class="job-country">U.K</div>
  <div class="job-title">Data Analyst</div><div class="job-type">Full-time</div>
  <p class="job-desc">Lorem ipsum dolor sit amet, consectetur adipis-cing elit, sed do eiusmod tempor incididunt ut labore et dolore magna aliqua. Quis ipsum sus-pendisse ultrices gravida. Risus commodo viverra</p>
  <div class="job-pay">$200/Month</div><div class="btn btn-outline">Apply Now</div>
</article>

<!-- how it works -->
<h2 class="abs section-title" style="left:120px;top:1338px;font-size:31px">How It Works &amp; Quick Feature</h2>
<div class="abs step active" style="top:1406px"><div class="step-num active">01</div><div><div class="step-title">Registered Account</div><div class="step-sub">First you need to make an account</div></div></div>
<div class="abs step-line" style="top:1446px"></div>
<div class="abs step" style="top:1478px"><div class="step-num">02</div><div><div class="step-title">List Your Job</div><div class="step-sub">List your job details</div></div></div>
<div class="abs step-line" style="top:1518px"></div>
<div class="abs step" style="top:1550px"><div class="step-num">03</div><div><div class="step-title">Search Candidate Near You</div><div class="step-sub">Search candidate near your location</div></div></div>
<div class="abs step-line" style="top:1590px"></div>
<div class="abs step" style="top:1622px"><div class="step-num">04</div><div><div class="step-title">Find The One</div><div class="step-sub">Find your desired one among thosands of job applicant.</div></div></div>

<div class="abs contact"></div>
<form class="abs contact-card">
  <h3>Contact Us Today</h3>
  <div class="field" style="top:60px">Name</div>
  <div class="field" style="top:109px">Phone</div>
  <div class="field" style="top:158px">Email</div>
  <div class="field" style="top:207px;height:65px">Message</div>
  <div class="btn btn-blue">SUBMIT</div>
</form>

<!-- business -->
<div class="abs" role="img" aria-label="Soft background of a desk with clipboard, paper clips and stationery" style="left:620px;top:1929px;width:580px;height:604px;background:radial-gradient(ellipse at 70% 40%,#e6e8ea 0%,#f1f2f3 45%,rgba(255,255,255,0) 75%)"></div>
<div class="abs photo" role="img" aria-label="Two engineers in hard hats, one holding a tablet and one a laptop" style="left:121px;top:1757px;width:468px;height:340px;background:linear-gradient(135deg,#3b4450 0%,#2a4f8f 40%,#d9673a 70%,#4a4f56 100%)"></div>
<div class="abs badge"><b>20k+</b><span>People Got Hired</span></div>
<h2 class="abs section-title" style="left:668px;top:1753px">What the business is about</h2>
<p class="abs body-copy" style="left:668px;top:1805px;width:370px">We source skilled workers directly from the Philippines to work in the UK. With offices , training locations and specialist recruiters we can find the highest quality indi-viduals to add value and resources to any UK buisness. We delivery quality based on vast experience over a number of years.</p>
<div class="btn btn-blue" style="left:668px;top:1943px;width:132px;height:36px;font-size:13px">Learn More</div>

<h2 class="abs recruit">We <em>recruit</em> the finest talent available<br>with our dedicated 200 strong team.<br>Our centres are highlighted in <em>red</em><br><em>dots</em> on the map.</h2>
<div class="abs" role="img" aria-label="Map of the Philippines with recruitment centres marked by red dots" style="left:691px;top:2131px;width:385px;height:325px;background:linear-gradient(160deg,#8fb0f2 0%,#7ca3ee 60%,#86aaf0 100%)"></div>

<!-- talent -->
<h2 class="abs section-title" style="left:0;width:1200px;top:2497px;text-align:center">Find The Best Talent</h2>
<div class="abs talent" style="left:-150px"><div class="talent-photo" role="img" aria-label="Candidate portrait" style="background:linear-gradient(160deg,#c9b7a6,#6a4a4a)"></div><span class="rating"><i>★</i>4.7</span></div>
<div class="abs talent" style="left:99px"><div class="talent-photo" role="img" aria-label="Portrait of a smiling man in a cap and work jacket" style="background:linear-gradient(160deg,#9fa7a0,#8d7a62 60%,#5f5a4f)"></div><span class="rating"><i>★</i>4.9</span>
  <div class="talent-role">Website Designer</div><div class="talent-name">Sam Lorenzo</div><div class="talent-age">33 Years old</div></div>
<div class="abs talent" style="left:350px"><div class="talent-photo" role="img" aria-label="Portrait of a smiling woman outdoors" style="background:linear-gradient(160deg,#a8b59a,#6b5447 55%,#2b3550)"></div><span class="rating"><i>★</i>4.6</span>
  <div class="talent-role">Graphic Designer</div><div class="talent-name">Nico Reyes</div><div class="talent-age">23 Years old</div></div>
<div class="abs talent" style="left:604px"><div class="talent-photo" role="img" aria-label="Portrait of a young man at sunset" style="background:linear-gradient(160deg,#e1a970,#b57a4f 45%,#2d2f3a)"></div><span class="rating"><i>★</i>3.8</span>
  <div class="talent-role">Web Developer</div><div class="talent-name">Vic Hanson</div><div class="talent-age">25 Years old</div></div>
<div class="abs talent" style="left:849px"><div class="talent-photo" role="img" aria-label="Portrait of a woman in a floral top" style="background:linear-gradient(160deg,#c8c0b8,#5c4640 50%,#22263a)"></div><span class="rating"><i>★</i>5.0</span>
  <div class="talent-role">Graphic Designer</div><div class="talent-name">Sara Gomez</div><div class="talent-age">29 Years old</div></div>
<div class="abs talent" style="left:1099px"><div class="talent-photo" role="img" aria-label="Portrait of a woman holding a notebook" style="background:linear-gradient(160deg,#d8cbb8,#a88f76)"></div>
  <div class="talent-role">Graphic Designer</div><div class="talent-name">Nico Reyes</div><div class="talent-age">23 Years old</div></div>
<span class="abs dot on" style="left:557px"></span><span class="abs dot" style="left:582px"></span><span class="abs dot" style="left:607px"></span><span class="abs dot" style="left:632px"></span>

<!-- where to start -->
<div class="abs photo" role="img" aria-label="Woman in a hard hat working at a metal workshop" style="left:121px;top:3002px;width:456px;height:338px;background:linear-gradient(135deg,#8c8c94 0%,#5d4a44 40%,#c47a4a 60%,#3b3c42 100%)"></div>
<h2 class="abs section-title" style="left:619px;top:3043px">Where to Start</h2>
<p class="abs body-copy" style="left:619px;top:3093px;width:455px">We need to know what your issues are and how we can understand the personnal you require , over what time frame and the number of employe-es you need. Once this is establisihed we start sourcing workers in the Philippines that meet your criteria while starting the process in the UK to be able to have all the documents in place to deliver your company hard working skilled individuals.</p>
<div class="btn btn-blue" style="left:619px;top:3219px;width:108px;height:45px;font-size:13px">Find A Talent</div>

<!-- footer -->
<footer class="abs footer">
  <h4 style="left:121px">Newsletter</h4>
  <div class="abs newsletter">
    <span class="abs" style="left:30px;top:15px;font-size:11.5px;color:#555">Email Address</span>
    <span class="btn" style="left:292px;top:9px;width:88px;height:27px;background:var(--red);color:var(--white);font-size:10px;border-radius:4px">SUBSCRIBE</span>
  </div>
  <h4 style="left:590px">Contacts</h4>
  <div class="contact-row" style="top:108px"><svg width="14" height="14" viewBox="0 0 24 24"><path d="M6.6 10.8a15 15 0 0 0 6.6 6.6l2.2-2.2c.3-.3.7-.4 1-.2 1.1.4 2.3.6 3.6.6.6 0 1 .4 1 1V20c0 .6-.4 1-1 1A17 17 0 0 1 3 4c0-.6.4-1 1-1h3.5c.6 0 1 .4 1 1 0 1.3.2 2.5.6 3.6.1.3 0 .7-.2 1z" fill="#111"/></svg>07700 900418</div>
  <div class="contact-row" style="top:136px"><svg width="14" height="12" viewBox="0 0 24 18"><rect x="1" y="1" width="22" height="16" fill="#111"/><path d="M1 1l11 9 11-9" fill="none" stroke="#f08f49" stroke-width="2"/></svg>sales@brindlestaffing.example.com</div>
  <div class="contact-row" style="top:162px"><svg width="12" height="16" viewBox="0 0 12 16"><path d="M6 0a6 6 0 0 0-6 6c0 4.5 6 10 6 10s6-5.5 6-10a6 6 0 0 0-6-6z" fill="#111"/><circle cx="6" cy="6" r="2.2" fill="#f08f49"/></svg><span>12 Orchard Row, Eastby<br>EB4 2 United Kingdom</span></div>
  <h4 style="left:833px">Quick Links</h4>
  <ul style="left:833px;top:109px"><li>Home</li><li>About Us</li><li>What we do</li><li>How we help</li><li>Where to start</li><li>Where to start</li></ul>
  <h4 style="left:983px">Jobs</h4>
  <ul style="left:984px;top:100px"><li>Civil engineer</li><li>Highways engineer</li><li>Petroleum engineer</li><li>Site engineer</li><li>Anthropologist</li><li>Criminologist</li><li>Epidemiologist</li><li>Other Jobs</li></ul>
</footer>
<div class="abs bottom-bar">
  <span class="abs" style="left:125px;top:14px">© 2023 All Rights Reserved | Brindle Staffing Ltd</span>
  <span class="abs social" style="left:941px" aria-label="Social link"></span>
  <span class="abs social" style="left:976px" aria-label="Social link"></span>
  <span class="abs social" style="left:1012px" aria-label="Social link"></span>
  <span class="abs social" style="left:1051px" aria-label="Social link"></span>
</div>

</body>
</html>
```